Law Office business card design

I have a general practice specializing in criminal defense work and domestic cases. I have extensive trial and appellate experience.

Target Market(s)

general public

Industry/Entity Type

Defense

Contact Information for Business Card

Dorrington Law Office, P.A.
382 N. 4th
PO Box 5284
Salina, KS 67409-5284
(785) 555-0172
(785) 555-0198 FAX
tdorrin@quellmail.net

Requirements
Must have
• A symbol that immediately identifes the card as a legal practice.

```html
<!DOCTYPE html>
<html lang="en">
<head>
<meta charset="utf-8">
<title>Dorrington Law Office, P.A. — Business Card</title>
<link rel="stylesheet" href="https://fonts.googleapis.com/css2?family=Lato:wght@400;700&display=swap">
<style>
  :root {
    --page-bg: #e9e6e1;
    --card-bg: #ffffff;
    --ink: #1b1b1b;
    --firm-red: #7a1f1a;
    --rule-red: #5e1512;
    --symbol-tone: #4a4a4a;
  }
  * { box-sizing: border-box; margin: 0; padding: 0; }
  html, body {
    width: 1200px;
    height: 735px;
    overflow: hidden;
    background: var(--page-bg);
    font-family: "Lato", sans-serif;
    color: var(--ink);
  }
  .business-card {
    position: absolute;
    left: 100px;
    top: 82px;
    width: 1000px;
    height: 571px;
    background: var(--card-bg);
    box-shadow: 0 10px 30px rgba(0,0,0,0.18);
  }
  .legal-symbol {
    position: absolute;
    left: 60px;
    top: 112px;
    width: 72px;
    height: 60px;
    background: linear-gradient(180deg, #6a6a6a, var(--symbol-tone));
    border-radius: 4px;
  }
  .firm-name {
    position: absolute;
    left: 250px;
    top: 108px;
    font-size: 40px;
    font-weight: 400;
    color: var(--firm-red);
    letter-spacing: 0.5px;
  }
  .header-rule {
    position: absolute;
    left: 150px;
    top: 172px;
    width: 720px;
    height: 6px;
  }
  .street-address {
    position: absolute;
    left: 200px;
    top: 208px;
    font-size: 26px;
  }
  .email {
    position: absolute;
    left: 650px;
    top: 262px;
    font-size: 22px;
  }
  .phone-lines {
    position: absolute;
    left: 140px;
    top: 420px;
    font-size: 24px;
    line-height: 1.4;
  }
</style>
</head>
<body>
  <div class="business-card">
    <div class="legal-symbol" role="img" aria-label="Scales of justice symbol"></div>
    <h1 class="firm-name">Dorrington Law Office, P.A.</h1>
    <svg class="header-rule" viewBox="0 0 720 6" preserveAspectRatio="none" aria-hidden="true">
      <rect x="0" y="0" width="720" height="6" rx="3" fill="var(--rule-red)"/>
    </svg>
    <p class="street-address">382 N. 4th PO Box 5284 Salina, KS 67409-5284</p>
    <p class="email">Email: tdorrin@quellmail.net</p>
    <div class="phone-lines">
      <p class="phone">Phone:&nbsp; 785-555-0172</p>
      <p class="fax">FAX: 785-555-0198</p>
    </div>
  </div>
</body>
</html>
```